Modern business card design

Looking for a modern business card layout with on the one side the logo (blue or white version) and on the other side the information such as name, email, phone numbers, website and QR code.
Enclosed the logo, the info and the QR code to be used. QR code should also give you all the info that could / should be on the card. Also enclosed a few examples of business cards I do like that should give you an idea what I am looking for. The "back of business card ideas" I like for the lay out, the modern business card idea is more because I do like the fact that the colour from the front is used again on the back so it is not just white.
Color codes: HS #D19B2A and HS #D19B2A
Fonts of the logo are: Heading Pro Treble Bold and SangBlue Sans/
See enclosed

```html
<!DOCTYPE html>
<html lang="en">
<head>
<meta charset="utf-8">
<title>Northwind Cargo – Business Card</title>
<link rel="stylesheet" href="https://fonts.googleapis.com/css2?family=Figtree:wght@400;500&display=swap">
<style>
  :root {
    --backdrop: #8c8c8c;
    --card-light: #ffffff;
    --card-mid: #e6e5e6;
    --card-shade: #c4c3c5;
    --ink: #111014;
    --rule: #2a1f33;
    --brand-blue: #2b3a97;
    --brand-gold: #d19b2a;
  }
  * { box-sizing: border-box; margin: 0; padding: 0; }
  html, body {
    width: 1160px;
    height: 1200px;
    overflow: hidden;
    background: var(--backdrop);
    font-family: "Figtree", sans-serif;
    color: var(--ink);
  }
  .card {
    position: absolute;
    left: 199px;
    width: 778px;
    height: 442px;
  }
  .card--info {
    top: 105px;
    background: linear-gradient(170deg, var(--card-light) 0%, var(--card-mid) 45%, var(--card-shade) 100%);
  }
  .card--brand {
    top: 634px;
    height: 444px;
    background: linear-gradient(170deg, var(--card-shade) 0%, var(--card-mid) 50%, var(--card-light) 100%);
  }
  .holder { position: absolute; top: 52px; left: 0; width: 100%; text-align: center; }
  .holder__name { font-size: 37px; font-weight: 500; letter-spacing: 0.5px; line-height: 1; }
  .holder__title { margin-top: 10px; font-size: 22px; font-weight: 400; }
  .rule { position: absolute; background: var(--rule); }
  .rule--top { left: 25px; top: 152px; width: 728px; height: 2px; }
  .rule--stem { width: 2px; height: 50px; top: 240px; }
  .rule--tag { top: 410px; height: 2px; width: 127px; }
  .icon { position: absolute; top: 173px; width: 52px; height: 48px; fill: var(--ink); }
  .contact { position: absolute; font-size: 20px; line-height: 28px; }
  .contact--phone { left: 29px; top: 298px; }
  .contact--mail { left: 238px; top: 297px; }
  .contact--web { left: 502px; top: 311px; }
  .services {
    position: absolute; left: 0; top: 366px; width: 100%;
    text-align: center; font-size: 20px; line-height: 28px;
  }
  .brand {
    position: absolute; top: 0; left: 0; width: 100%; height: 100%;
    display: flex; align-items: center; justify-content: center; gap: 18px;
  }
  .brand__dot { width: 26px; height: 26px; border-radius: 50%; background: var(--brand-gold); }
  .brand__name {
    font-size: 54px; font-weight: 500; letter-spacing: 6px;
    color: var(--brand-blue); line-height: 1;
  }
</style>
</head>
<body>
  <section class="card card--info">
    <header class="holder">
      <h1 class="holder__name">DANIEL REYES</h1>
      <p class="holder__title">Creative Director</p>
    </header>
    <div class="rule rule--top"></div>

    <svg class="icon" style="left:70px" viewBox="0 0 24 24" aria-label="Phone">
      <path d="M6.6 2.5 9.3 6.4c.4.6.3 1.3-.2 1.8L7.6 9.6c1.2 2.6 3.6 5 6.2 6.3l1.4-1.5c.5-.5 1.2-.6 1.8-.2l3.9 2.6c.6.4.8 1.2.4 1.8l-1.2 2.1c-.4.7-1.2 1.1-2 1C9.6 21 3 14.4 2.3 6.1c-.1-.8.3-1.6 1-2l2.1-1.2c.4-.3.9-.2 1.2.1zM13 2.2a9 9 0 0 1 8.8 8.8h-2.1A6.9 6.9 0 0 0 13 4.3zm0 3.7a5.2 5.2 0 0 1 5.1 5.1H16A3.1 3.1 0 0 0 13 8z"/>
    </svg>
    <svg class="icon" style="left:273px" viewBox="0 0 26 20" aria-label="Email">
      <path d="M1.5 0h23c.8 0 1.5.7 1.5 1.5v.4L13 11 0 1.9v-.4C0 .7.7 0 1.5 0zM0 4.2l8.6 6L0 17.4zm26 0v13.2l-8.6-7.2zM10.3 11.4 13 13.3l2.7-1.9 9.6 8H1.5c-.3 0-.5 0-.7-.1z"/>
    </svg>
    <svg class="icon" style="left:612px" viewBox="0 0 24 24" aria-label="Website">
      <circle cx="12" cy="12" r="11"/>
      <path d="M6 6.5c1.8-1.2 3.6-.6 4.4.6.7 1-.2 2.4-1.4 2.6-1.4.3-1.6 1.8-.6 2.8 1 1 .4 3-1 3.6-.9-1.2-1.7-3-2.2-4.7C4.7 9.6 5 7.8 6 6.5zm8.2-2.4c1.6.2 3.8 1.4 4.8 3.2-1 .6-2.2.2-3 1-.8.7-.2 2 .8 2.3 1.4.4 2.4 1.6 1.8 3.4-.7 1.8-2.2 3.4-3.8 4-.4-1.6.4-3-.6-4.2-1-1-2.6-1.4-2.4-3 .2-1.4 1.8-1.6 2.6-2.6.6-.8.2-1.6-.2-2.1z" fill="#eeeeee"/>
    </svg>

    <div class="rule rule--stem" style="left:98px"></div>
    <div class="rule rule--stem" style="left:301px"></div>
    <div class="rule rule--stem" style="left:641px"></div>

    <p class="contact contact--phone">+971500123456<br>+32470112233</p>
    <p class="contact contact--mail">marco.lindqvist<br>@northwindcargo.com</p>
    <p class="contact contact--web">www.northwindcargo.com</p>

    <p class="services">Strategy - Operational Efficiency - Digitalization - Change Management -<br>Business Development - Connecting People</p>
    <div class="rule rule--tag" style="left:50px"></div>
    <div class="rule rule--tag" style="left:606px"></div>
  </section>

  <section class="card card--brand">
    <div class="brand">
      <span class="brand__dot"></span>
      <span class="brand__name">NORTHWIND CARGO</span>
    </div>
  </section>
</body>
</html>
```